New Software Development Firm Needs Business Cards!

We just completed a successful logo design project on MakerHive and need to develop a business card design using that shiny new logo. We want a clean, modern design that communicates professionalism and tech savvy without being cliche'.

The company is "Bramble Logic, LLC", but our dba is "Bramble" The business card address should reflect the full company name in the address. The logo just uses "Bramble".

Photoshop or Illustrator source files will be required, along with exact font name(s) and source(s) used.

The design will need to work well with our letterhead as well. I'm also launching a project right now for letterhead and envelopes as well. Please submit to both projects! We're excited to see the designs. Thanks...

Target Market(s)

Small to medium business professionals

Industry/Entity Type

Business

Requirements
Must have
• Need place for:
- Company name and address (5 lines)
- Phone: (1 number)
- Fax: (1 number)
- Employee's name
- Employee's position
- Employee's email address
- Company web site URL
Nice to have
• Probably want a white card, but we're open to options.

```html
<!DOCTYPE html>
<html lang="en">
<head>
<meta charset="utf-8">
<title>Bramble — Business Card</title>
<link rel="stylesheet" href="https://fonts.googleapis.com/css2?family=Fira+Sans+Condensed:wght@400;500&display=swap">
<style>
  :root {
    --stage: #e4e4e6;
    --paper: #ffffff;
    --ink: #111111;
    --card-black: #0d0d0d;
    --accent-red: #e0232a;
    --muted-line: #3a3a3a;
  }
  * { box-sizing: border-box; margin: 0; padding: 0; }
  html, body { width: 1200px; height: 960px; overflow: hidden; }
  body {
    background: var(--stage);
    font-family: "Fira Sans Condensed", "Arial Narrow", sans-serif;
    color: var(--ink);
    display: flex;
    flex-direction: column;
    align-items: center;
    justify-content: center;
    gap: 40px;
  }
  .card {
    position: relative;
    width: 760px;
    height: 434px;
    overflow: hidden;
    box-shadow: 0 6px 18px rgba(0,0,0,0.18);
  }
  .card--front { background: var(--paper); }
  .card--back {
    background: var(--card-black);
    display: flex;
    align-items: center;
    justify-content: center;
  }
  .brand-name {
    font-weight: 500;
    letter-spacing: 1px;
    line-height: 1;
  }
  .card--front .brand-name {
    position: absolute;
    left: 78px;
    top: 176px;
    font-size: 78px;
    color: var(--ink);
  }
  .card--back .brand-name {
    font-size: 74px;
    letter-spacing: 4px;
    color: var(--paper);
  }
  .divider {
    position: absolute;
    left: 426px;
    top: 52px;
    width: 2px;
    height: 310px;
    background: var(--muted-line);
  }
  .person {
    position: absolute;
    left: 456px;
    top: 50px;
  }
  .person__name { font-size: 33px; font-weight: 400; line-height: 1.1; }
  .person__role { font-size: 19px; line-height: 1.2; }
  .contact-list {
    position: absolute;
    left: 456px;
    top: 134px;
    list-style: none;
    font-size: 18px;
    line-height: 25px;
  }
  .contact-list li { display: flex; align-items: flex-start; gap: 8px; }
  .contact-list svg { width: 15px; height: 15px; margin-top: 5px; flex: none; fill: var(--accent-red); }
  .contact-list .indent { padding-left: 23px; }
  .contact-list .company { font-weight: 500; }
  .contact-list .gap { margin-top: 4px; }
  .footer-bands {
    position: absolute;
    left: 0; bottom: 0;
    width: 100%; height: 52px;
  }
  .website {
    position: absolute;
    right: 34px;
    bottom: 12px;
    font-size: 17px;
    color: var(--paper);
  }
</style>
</head>
<body>
  <section class="card card--front" aria-label="Business card front">
    <div class="brand-name">Bramble</div>
    <div class="divider"></div>
    <div class="person">
      <div class="person__name">Alex Moreno</div>
      <div class="person__role">Director</div>
    </div>
    <ul class="contact-list">
      <li class="company"><svg viewBox="0 0 16 16" aria-hidden="true"><path d="M8 1 1 8h2v7h4v-4h2v4h4V8h2z"/></svg>Bramble Logic, LLC</li>
      <li class="indent">42 Larkin Avenue</li>
      <li class="indent">Suite 210</li>
      <li class="indent">Riverton, ST 54021</li>
      <li class="indent">United States</li>
      <li class="gap"><svg viewBox="0 0 16 16" aria-hidden="true"><path d="M4 1 6.5 4 5 6c1 2 3 4 5 5l2-1.5 3 2.5-2 2.5C7 14 2 9 1.5 3.5z"/></svg>555-218-4730</li>
      <li><svg viewBox="0 0 16 16" aria-hidden="true"><path d="M4 1h8v4H4zM1 6h14v6h-3v3H4v-3H1zM5 10v3h6v-3z"/></svg>555-218-4731</li>
      <li><svg viewBox="0 0 16 16" aria-hidden="true"><path d="M1 3h14v10H1zM2 4.5v.5l6 4 6-4v-.5z"/></svg>hello@bramblelogic.example</li>
    </ul>
    <svg class="footer-bands" viewBox="0 0 760 52" preserveAspectRatio="none" aria-hidden="true">
      <rect x="0" y="38" width="500" height="14" fill="var(--accent-red)"/>
      <polygon points="506,52 520,10 760,0 760,52" fill="var(--card-black)"/>
    </svg>
    <div class="website">www.bramblelogic.example</div>
  </section>

  <section class="card card--back" aria-label="Business card back">
    <div class="brand-name">Bramble</div>
  </section>
</body>
</html>
```